Design a Professional Business Card for Vello Marra

Design a business card for Vello Marra, we are a National Sport Court Company.

West Region Address: 4172 Glen Harrow Ct, Suite #210 Pine Hollow, Westland 00412
East Region Address: 7316 38th Ave W, Marrow Bay, Eastland 00718

Target Market(s)

High End Residential & Institutional Clients

Industry/Entity Type

Design & Construction

Contact Information for Business Card

Logo/Brand/Colors/ name, number (provided in comments)

Requirements
Must have
• Colors only provided in logo
Should not have
• Any other colors not in existing logo (attached)

```html
<!DOCTYPE html>
<html lang="en">
<head>
<meta charset="utf-8">
<title>Vello Marra – Business Card</title>
<link rel="stylesheet" href="https://fonts.googleapis.com/css2?family=Poppins:wght@400;600;700&display=swap">
<style>
  :root {
    --navy: #1d3a6e;
    --green: #1a6b38;
    --white: #ffffff;
    --stage: #2a2b2e;
    --rule: #5e9a6e;
    --ink: #1c1c1c;
  }
  * { box-sizing: border-box; margin: 0; padding: 0; }
  html, body { width: 1200px; height: 1200px; overflow: hidden; }
  body {
    background: var(--stage);
    font-family: "Poppins", sans-serif;
    position: relative;
  }
  .card {
    position: absolute;
    left: 160px;
    width: 880px;
    height: 503px;
    box-shadow: 0 18px 40px rgba(0,0,0,0.45);
  }
  .card--front {
    top: 72px;
    background: linear-gradient(180deg, var(--navy) 0%, #1a5555 50%, var(--green) 100%);
    display: flex;
    align-items: center;
    justify-content: center;
  }
  .card--back {
    top: 625px;
    background: var(--white);
  }
  .brand {
    display: flex;
    align-items: center;
    gap: 26px;
  }
  .brand__dot {
    border-radius: 50%;
    flex: none;
  }
  .brand__name {
    font-weight: 700;
    text-transform: uppercase;
    line-height: 0.95;
    letter-spacing: 0.06em;
  }
  .card--front .brand__dot { width: 112px; height: 112px; background: var(--white); }
  .card--front .brand__name { color: var(--white); font-size: 56px; }

  .card--back .brand {
    position: absolute;
    left: 62px;
    top: 52px;
  }
  .card--back .brand__dot { width: 126px; height: 126px; background: var(--navy); }
  .card--back .brand__name { color: var(--navy); font-size: 62px; }

  .person {
    position: absolute;
    left: 62px;
    top: 258px;
    width: 370px;
  }
  .person__name {
    color: var(--navy);
    font-weight: 700;
    font-size: 29px;
    letter-spacing: 0.02em;
    text-transform: uppercase;
    line-height: 1.1;
  }
  .person__role {
    color: var(--green);
    font-size: 20px;
    line-height: 1.2;
  }
  .person__rule {
    border: 0;
    border-top: 1px solid var(--rule);
    margin: 14px 0 22px;
  }
  .contact { list-style: none; }
  .contact__item {
    display: flex;
    align-items: center;
    gap: 14px;
    color: var(--ink);
    font-size: 20px;
    line-height: 1.55;
  }
  .contact__icon {
    width: 22px; height: 22px;
    flex: none;
  }
  .offices {
    position: absolute;
    left: 510px;
    top: 296px;
    width: 340px;
  }
  .office + .office { margin-top: 16px; }
  .office__label {
    color: var(--green);
    font-weight: 600;
    font-size: 15px;
    text-transform: uppercase;
    letter-spacing: 0.03em;
  }
  .office__address {
    color: var(--navy);
    font-size: 17px;
    line-height: 1.3;
    font-style: normal;
  }
</style>
</head>
<body>
  <section class="card card--front" aria-label="Business card front">
    <div class="brand">
      <span class="brand__dot"></span>
      <p class="brand__name">Vello<br>Marra</p>
    </div>
  </section>

  <section class="card card--back" aria-label="Business card back">
    <div class="brand">
      <span class="brand__dot"></span>
      <p class="brand__name">Vello<br>Marra</p>
    </div>

    <div class="person">
      <h1 class="person__name">Dorian Pell</h1>
      <p class="person__role">Manager</p>
      <hr class="person__rule">
      <ul class="contact">
        <li class="contact__item">
          <svg class="contact__icon" viewBox="0 0 22 22" aria-hidden="true">
            <circle cx="11" cy="11" r="11" fill="var(--green)"/>
            <rect x="7.5" y="5" width="7" height="12" rx="1.2" fill="none" stroke="#fff" stroke-width="1.6"/>
          </svg>
          555-214-0687
        </li>
        <li class="contact__item">
          <svg class="contact__icon" viewBox="0 0 22 22" aria-hidden="true">
            <circle cx="11" cy="11" r="11" fill="var(--green)"/>
            <rect x="5.5" y="7" width="11" height="8" fill="none" stroke="#fff" stroke-width="1.4"/>
            <path d="M5.5 7 L11 11.5 L16.5 7" fill="none" stroke="#fff" stroke-width="1.4"/>
          </svg>
          office@vellomarra.com
        </li>
      </ul>
    </div>

    <div class="offices">
      <div class="office">
        <h2 class="office__label">West Region Address</h2>
        <address class="office__address">4172 Glen Harrow Ct,<br>Suite #210 Pine Hollow,<br>Westland 00412</address>
      </div>
      <div class="office">
        <h2 class="office__label">East Region Address</h2>
        <address class="office__address">7316 38th Ave W, Marrow Bay,<br>Eastland 00718</address>
      </div>
    </div>
  </section>
</body>
</html>
```